Graphic to hang inside of fitness studio

This graphic will be printed on vinyl and hung inside of a boutique fitness studio for 2019. Graphic should read YEAR OF POSSIBILITIES.

2018 was called Year of Living Well. We would like something on trend for 2019 to hang within the studio as our 2019 Mantra. It is not a logo but for internal use. I've attached our logo here and the website is www.kestrelmovehall.com for additional reference. Thank you.

Target Market(s)

25 to 45 women

Industry/Entity Type

Fitness

Colors

Designer to choose colors to be used in the design.

Requirements
Must have
• On trend for 2019. (no people in image)
• Year of Possibilities in trendy font.
• Easy to read.
• Need text only.
• Do not need graphic images.
Nice to have
• Tintorell colours for 2019
• 2019 design trends for background
Should not have
• Male dominate colour or masculine traits.
• Photos of fitness.
• Photos of people.
• Photos of equipment.

```html
<!DOCTYPE html>
<html lang="en">
<head>
<meta charset="utf-8">
<title>Year of Possibilities – Kestrel Move Hall 2019 Mantra</title>
<link rel="stylesheet" href="https://fonts.googleapis.com/css2?family=Bodoni+Moda:wght@400;700&display=swap">
<style>
  :root {
    --coral: #f4705f;
    --coral-soft: #f6887a;
    --coral-tint: #f9b0a5;
    --teal: #00999c;
    --teal-tint: #7cc6c7;
    --sky: #a2d2dc;
    --paper: #ffffff;
  }
  html, body {
    margin: 0;
    padding: 0;
    overflow: hidden;
    background: var(--paper);
  }
  .mantra-board {
    position: relative;
    width: 1200px;
    height: 600px;
    overflow: hidden;
    background: var(--paper);
  }
  .geometry {
    position: absolute;
    inset: 0;
    width: 1200px;
    height: 600px;
  }
  .fill-coral { fill: var(--coral); }
  .fill-coral-soft { fill: var(--coral-soft); }
  .fill-coral-tint { fill: var(--coral-tint); }
  .fill-teal { fill: var(--teal); }
  .fill-teal-tint { fill: var(--teal-tint); }
  .fill-sky { fill: var(--sky); }

  .headline {
    position: absolute;
    margin: 0;
    font-family: "Bodoni Moda", "Didot", serif;
    font-weight: 400;
    color: var(--teal);
    line-height: 1;
    white-space: nowrap;
    transform-origin: left top;
  }
  .headline-year {
    left: 527px;
    top: 104px;
    font-size: 74px;
    letter-spacing: 2px;
    transform: scaleX(0.99) scaleY(1.18);
  }
  .headline-of {
    left: 757px;
    top: 164px;
    font-size: 40px;
    letter-spacing: 1px;
    transform: scaleX(0.86) scaleY(1.1);
  }
  .headline-possibilities {
    left: 603px;
    top: 222px;
    font-size: 76px;
    letter-spacing: 3px;
    transform: scaleX(0.95) scaleY(1.15);
  }
  .studio-name {
    position: absolute;
    left: 772px;
    top: 396px;
    margin: 0;
    font-family: "Bodoni Moda", "Didot", serif;
    font-weight: 700;
    font-size: 13px;
    letter-spacing: 0.2px;
    color: var(--teal);
    white-space: nowrap;
  }
  .studio-mark {
    position: absolute;
    left: 827px;
    top: 358px;
    width: 22px;
    height: 22px;
    border-radius: 50%;
    background: var(--teal);
  }
</style>
</head>
<body>
<main class="mantra-board">
  <svg class="geometry" viewBox="0 0 1200 600">
    <defs>
      <radialGradient id="burst-glow" cx="0.5" cy="0.5" r="0.5">
        <stop offset="0" stop-color="#ffffff" stop-opacity="0"/>
        <stop offset="0.25" stop-color="#f9b0a5" stop-opacity="0.9"/>
        <stop offset="1" stop-color="#f6887a" stop-opacity="0.75"/>
      </radialGradient>
    </defs>

    <!-- top row tiles -->
    <rect class="fill-coral" x="0" y="0" width="150" height="150"/>
    <rect class="fill-coral-tint" x="150" y="0" width="145" height="150" role="img" aria-label="Coral stripe texture tile"/>
    <polygon class="fill-coral" points="300,150 450,0 450,150"/>

    <!-- left column -->
    <rect class="fill-teal" x="0" y="150" width="150" height="300"/>
    <circle class="fill-sky" cx="75" cy="225" r="75"/>
    <rect class="fill-coral-soft" x="10" y="305" width="130" height="140" role="img" aria-label="Coral dot texture on teal"/>
    <polygon class="fill-sky" points="150,150 300,150 150,300"/>

    <!-- sky sweep behind the burst -->
    <path class="fill-sky" d="M450 150 L450 450 L292 450 Q430 430 450 150 Z"/>

    <!-- burst area -->
    <circle cx="292" cy="300" r="140" fill="url(#burst-glow)" role="img" aria-label="Radiating coral dot burst"/>

    <!-- upper middle -->
    <rect class="fill-sky" x="450" y="0" width="75" height="215"/>
    <rect class="fill-coral-tint" x="458" y="40" width="132" height="66" role="img" aria-label="Rows of coral dots"/>
    <rect class="fill-coral-soft" x="600" y="0" width="75" height="75"/>
    <rect class="fill-teal" x="750" y="75" width="75" height="75"/>
    <rect class="fill-coral-soft" x="900" y="0" width="150" height="150"/>

    <rect class="fill-coral-tint" x="450" y="230" width="150" height="70" role="img" aria-label="Coral horizontal stripe band"/>

    <!-- teal quarter -->
    <path class="fill-teal" d="M450 300 A150 150 0 0 1 600 450 L450 450 Z"/>

    <!-- arc band -->
    <path class="fill-coral-tint" d="M620 450 A130 130 0 0 1 750 320 L750 400 A50 50 0 0 0 700 450 Z" role="img" aria-label="Concentric coral arcs"/>

    <!-- lower left -->
    <rect class="fill-coral" x="0" y="450" width="150" height="75"/>
    <path class="fill-coral" d="M0 600 A75 75 0 0 1 150 600 Z"/>
    <polygon class="fill-teal" points="150,450 300,450 150,600"/>
    <path class="fill-coral" d="M300 600 Q300 450 450 450 L450 600 Z"/>

    <rect class="fill-coral-tint" x="490" y="450" width="70" height="150" role="img" aria-label="Coral vertical stripe band"/>

    <!-- dotted quadrant -->
    <path class="fill-coral-tint" d="M750 470 A130 130 0 0 1 880 600 L820 600 A70 70 0 0 0 750 530 Z" role="img" aria-label="Quarter ring of coral dots"/>

    <!-- right accents -->
    <circle class="fill-sky" cx="900" cy="450" r="22"/>
    <path class="fill-teal" d="M1050 380 A75 75 0 0 0 1050 530 Z"/>
    <path class="fill-teal-tint" d="M1050 455 L1125 455 A75 75 0 0 1 1050 530 Z" role="img" aria-label="Teal stripe fill"/>
    <path class="fill-coral-tint" d="M1200 452 L1200 600 L1050 600 Q1160 560 1200 452 Z" role="img" aria-label="Coral stripe corner sweep"/>
  </svg>

  <h1 class="headline headline-year">YEAR</h1>
  <p class="headline headline-of">OF</p>
  <p class="headline headline-possibilities">POSSIBILITIES</p>

  <span class="studio-mark" aria-hidden="true"></span>
  <p class="studio-name">KESTREL MOVE HALL</p>
</main>
</body>
</html>
```